Polish & Pause Headlight Restoration Kit

We have a product called "Polish & Pause: Headlight Restoration Kit" that we designed a couple years ago. Because it is very easy to use we sell a decent amount on Bazely but the packaging is 2-dimensional and does not do the product justice. Because our new product's packaging is so nice, this old product packaging makes Polish & Pause look like it's not even part of the Copper Fern product line!

We are looking to overhaul the packaging and make it much more attractive looking.

```html
<!DOCTYPE html>
<html lang="en">
<head>
<meta charset="utf-8">
<title>Polish &amp; Pause: Headlight Restoration Kit</title>
<link rel="stylesheet" href="https://fonts.googleapis.com/css2?family=Arvo:ital,wght@0,700;1,700&family=Open+Sans:wght@600;700&family=Exo+2:ital,wght@1,900&display=swap">
<style>
  :root {
    --black: #0b0b0b;
    --orange: #f26522;
    --orange-bright: #f47a2c;
    --red: #e3262b;
    --red-deep: #c81f26;
    --brown-dark: #2a0f09;
    --yellow: #fff200;
    --white: #ffffff;
  }
  * { margin: 0; padding: 0; box-sizing: border-box; }
  html, body { width: 1173px; height: 1200px; overflow: hidden; background: var(--white); }
  .panel {
    position: absolute; left: 137px; top: 150px;
    width: 898px; height: 898px;
    background: var(--black); overflow: hidden;
  }
  .layer { position: absolute; left: 0; top: 0; }
  .brand {
    position: absolute; left: 0; right: 0; top: 62px;
    display: flex; justify-content: center; align-items: center; gap: 12px;
    font-family: "Open Sans", sans-serif; font-weight: 700;
    font-size: 34px; color: var(--white); letter-spacing: 1px;
  }
  .brand-mark { width: 18px; height: 18px; background: var(--orange); }
  .badge {
    position: absolute; left: 808px; top: 75px;
    transform: translate(-50%, -50%) rotate(37deg);
    text-align: center; line-height: 1.05;
    font-family: "Arvo", serif; font-weight: 700; font-size: 27px;
    color: var(--yellow);
    -webkit-text-stroke: 1.5px var(--black); paint-order: stroke fill;
    white-space: nowrap;
  }
  .headline {
    position: absolute; left: 0; right: 0; top: 190px;
    text-align: center;
    font-family: "Arvo", serif; font-weight: 700; font-size: 74px;
    color: var(--orange); line-height: 1;
  }
  .tagline-band {
    position: absolute; left: 0; top: 290px; width: 100%; height: 75px;
    background: linear-gradient(90deg, var(--orange) 0%, #a34420 35%, #4a1a0e 70%, var(--brown-dark) 100%);
    display: flex; align-items: center; justify-content: center;
    font-family: "Open Sans", sans-serif; font-weight: 600; font-size: 31px; color: var(--white);
  }
  .product-title {
    position: absolute; left: 0; right: 0; top: 372px;
    text-align: center;
    font-family: "Exo 2", sans-serif; font-style: italic; font-weight: 900;
    font-size: 60px; letter-spacing: -1px; color: var(--orange); line-height: 1.2;
  }
  .result-photo {
    position: absolute; left: 204px; top: 472px; width: 424px; height: 247px;
    background: linear-gradient(100deg, #8a8f96 0%, #c9ccd1 30%, #4f6a9a 60%, #7a1a16 100%);
  }
  .tab {
    position: absolute; background: var(--black); color: var(--white);
    font-family: "Open Sans", sans-serif; font-weight: 700; font-size: 32px;
    display: flex; align-items: center;
  }
  .tab-before {
    left: 0; top: 479px; width: 245px; height: 57px; padding-left: 26px;
    clip-path: polygon(0 0, 88% 0, 100% 100%, 0 100%);
  }
  .tab-after {
    left: 605px; top: 585px; width: 293px; height: 60px; padding-left: 70px;
    clip-path: polygon(0 0, 100% 0, 100% 100%, 10% 100%);
  }
  .benefits {
    position: absolute; left: 0; top: 719px; width: 100%; height: 179px;
  }
  .benefit {
    position: absolute; display: flex; align-items: baseline; gap: 16px;
    font-family: "Open Sans", sans-serif; font-weight: 600; font-size: 24px; color: var(--white);
  }
  .benefit-word {
    font-family: "Arvo", serif; font-style: italic; font-weight: 700;
    font-size: 48px; color: var(--orange);
  }
  .benefit-polish { left: 116px; top: 20px; }
  .benefit-pause { left: 134px; top: 84px; }
</style>
</head>
<body>
<div class="panel">
  <svg class="layer" width="898" height="898" viewBox="0 0 898 898" aria-hidden="true">
    <defs>
      <linearGradient id="cornerGrad" x1="0" y1="0" x2="1" y2="1">
        <stop offset="0" stop-color="#f26522"/>
        <stop offset="1" stop-color="#8a2c12"/>
      </linearGradient>
      <linearGradient id="bottomGrad" x1="0" y1="0" x2="1" y2="0">
        <stop offset="0" stop-color="#1e0b07"/>
        <stop offset="0.45" stop-color="#4a170c"/>
        <stop offset="0.75" stop-color="#b8401c"/>
        <stop offset="1" stop-color="#e3262b"/>
      </linearGradient>
    </defs>
    <polygon points="605,0 898,0 898,216" fill="url(#cornerGrad)"/>
    <!-- stripe field behind the before/after area -->
    <rect x="0" y="472" width="898" height="247" fill="#e3262b"/>
    <polygon points="0,520 60,472 220,472 0,719" fill="#c81f26"/>
    <polygon points="40,719 250,472 330,472 120,719" fill="#f26522" opacity="0.85"/>
    <polygon points="560,472 640,472 860,719 780,719" fill="#f47a2c" opacity="0.8"/>
    <polygon points="820,472 898,472 898,719 870,719" fill="#ee3a24"/>
    <!-- bottom band -->
    <rect x="0" y="719" width="898" height="179" fill="url(#bottomGrad)"/>
    <polygon points="620,719 700,719 860,898 790,898" fill="#f47a2c" opacity="0.55"/>
    <polygon points="760,719 898,719 898,898 880,898" fill="#e3262b" opacity="0.7"/>
  </svg>

  <div class="brand"><span class="brand-mark"></span>Copper Fern</div>
  <div class="badge">Guaranteed<br>Easy!</div>

  <h1 class="headline">Polish &amp; Pause</h1>
  <div class="tagline-band">See the road better at night in minutes!</div>
  <h2 class="product-title">HEADLIGHT RESTORATION</h2>

  <div class="result-photo" role="img" aria-label="Car headlight split down the middle: cloudy, yellowed lens on the left, clear restored lens on the right"></div>
  <div class="tab tab-before">From this...</div>
  <div class="tab tab-after">...to this</div>

  <div class="benefits">
    <p class="benefit benefit-polish"><span class="benefit-word">Polish</span>your headlights to clarity in minutes.</p>
    <p class="benefit benefit-pause"><span class="benefit-word">Pause</span>and drive safely all night.</p>
  </div>
</div>
</body>
</html>
```